Vitaroot gym flyer

Use the text offered in the word document and add the appropriate images in the space provided. The images may need to be resized.Can the font be bold and silver with a black outline.Can the background be light blue.I have submitted a design request for some business cards. I'd like the cards and the flyer to match.

Industry/Entity Type

Gym

```html
<!DOCTYPE html>
<html lang="en">
<head>
<meta charset="utf-8">
<title>Vitaroot Body Transformation Flyer</title>
<link href="https://fonts.googleapis.com/css2?family=Russo+One&family=Oswald:wght@500;600&family=Quicksand:wght@600&family=Hind:wght@400;600&display=swap" rel="stylesheet">
<style>
  :root{
    --page-bg:#e4e4e6;
    --sky-light:#a9d2f0;
    --sky-mid:#7fb6e4;
    --sky-deep:#5b98d3;
    --silver-hi:#ffffff;
    --silver-lo:#b9c2cc;
    --ink:#111111;
    --tag-ink:#2c3440;
    --accent:#1e6fc4;
    --card:#f7f7f7;
    --pill:#6aaae0;
    --pill-edge:#ffffff;
  }
  html,body{margin:0;padding:0;width:1200px;height:1200px;overflow:hidden;background:var(--page-bg);}
  .flyer{
    position:absolute;left:191px;top:15px;width:818px;height:1170px;overflow:hidden;
    background:
      radial-gradient(ellipse 70% 42% at 50% 18%, rgba(255,255,255,.28), rgba(255,255,255,0) 70%),
      linear-gradient(180deg,var(--sky-deep) 0%,var(--sky-mid) 45%,var(--sky-light) 80%,var(--sky-light) 100%);
    box-shadow:0 6px 18px rgba(0,0,0,.25);
  }
  .arc{position:absolute;left:0;top:0;width:818px;height:1170px;}
  .headline{
    position:absolute;left:0;width:100%;text-align:center;margin:0;
    font-family:"Russo One",sans-serif;font-size:32px;line-height:40px;
    transform:skewX(-10deg) scaleX(1.2);
    background:linear-gradient(180deg,var(--silver-hi) 0%,#e6eaee 45%,var(--silver-lo) 100%);
    -webkit-background-clip:text;background-clip:text;color:transparent;
    -webkit-text-stroke:1.6px var(--ink);
    filter:drop-shadow(2px 3px 2px rgba(0,0,0,.45));
    letter-spacing:-1px;white-space:nowrap;
  }
  .headline--question{top:56px;font-size:31px;}
  .headline--intro{top:136px;}
  .headline--coach{top:864px;line-height:42px;}
  .story{
    position:absolute;background:var(--card);
    box-shadow:2px 4px 8px rgba(0,0,0,.3);
  }
  .story--lauren{left:47px;top:309px;width:335px;height:397px;transform:rotate(.8deg);}
  .story--stuart{left:443px;top:306px;width:345px;height:408px;transform:rotate(-2.2deg);}
  .story__photos{position:absolute;left:16px;top:12px;right:12px;height:282px;display:flex;gap:3px;}
  .story__photo{flex:1;}
  .photo--lauren-before{background:linear-gradient(160deg,#6a6872,#2c2a33 70%,#7a6a62);}
  .photo--lauren-after{background:linear-gradient(170deg,#d9d2c6,#a69a8c 60%,#3a3432);}
  .photo--stuart-before{background:linear-gradient(170deg,#6f8a52,#a7a9a4 55%,#5d6a3f);}
  .photo--stuart-after{background:linear-gradient(170deg,#e7e3da,#c9a48d 55%,#2a2a2a);}
  .pin{position:absolute;top:-24px;width:26px;height:40px;}
  .pill{
    position:absolute;top:260px;width:118px;height:32px;border-radius:8px;
    background:linear-gradient(180deg,#8cc0ea,var(--pill));
    border:2px solid var(--pill-edge);box-shadow:0 1px 3px rgba(0,0,0,.25);
    font-family:"Quicksand",sans-serif;font-size:18px;color:#fff;text-align:center;line-height:32px;
  }
  .story__caption{position:absolute;left:0;right:0;top:304px;text-align:center;font-family:"Hind",sans-serif;color:#1b1b1b;}
  .story__name{font-size:22px;font-weight:600;line-height:26px;}
  .story__detail{font-size:17px;line-height:22px;}
  .tagline{
    position:absolute;left:0;width:100%;text-align:center;margin:0;
    font-family:"Oswald",sans-serif;font-weight:500;font-size:37px;color:var(--tag-ink);
    transform:skewX(-12deg) scaleX(.86);letter-spacing:-.5px;
  }
  .tagline--one{top:758px;}
  .tagline--two{top:814px;}
  .tagline__keep{color:var(--accent);text-decoration:underline;text-decoration-thickness:2px;margin-left:12px;}
  .swoosh{position:absolute;left:0;bottom:0;width:818px;height:140px;}
  .contact{
    position:absolute;right:48px;text-align:right;margin:0;
    font-family:"Russo One",sans-serif;color:var(--accent);transform:skewX(-12deg);
    text-shadow:2px 3px 3px rgba(0,0,0,.3);
  }
  .contact--phone{top:1050px;font-size:30px;}
  .contact--social{top:1094px;font-size:29px;letter-spacing:-.5px;}
</style>
</head>
<body>
<main class="flyer">
  <svg class="arc" viewBox="0 0 818 1170" aria-hidden="true">
    <path d="M-40 1170 L-40 760 Q-40 40 409 40 Q858 40 858 760 L858 1170 Z" fill="rgba(255,255,255,.12)"/>
  </svg>

  <h1 class="headline headline--question">Are you happy with your body shape?</h1>
  <p class="headline headline--intro">Would you like to improve your health<br>&amp; energy levels at the same time as<br>transforming your body shape?</p>

  <article class="story story--lauren">
    <svg class="pin" style="left:172px" viewBox="0 0 26 40" aria-hidden="true"><ellipse cx="13" cy="9" rx="11" ry="7" fill="#5fb2e8"/><rect x="8" y="9" width="10" height="14" fill="#4aa2dc"/><line x1="13" y1="23" x2="11" y2="38" stroke="#888" stroke-width="2"/></svg>
    <div class="story__photos">
      <div class="story__photo photo--lauren-before" role="img" aria-label="Before photo of Lauren"></div>
      <div class="story__photo photo--lauren-after" role="img" aria-label="After photo of Lauren"></div>
    </div>
    <div class="pill" style="left:32px">Before</div>
    <div class="pill" style="left:188px">After</div>
    <div class="story__caption">
      <div class="story__name">Lauren Ridley</div>
      <div class="story__detail">Payroll Supervisor</div>
      <div class="story__detail">Age - 27</div>
    </div>
  </article>

  <article class="story story--stuart">
    <svg class="pin" style="left:162px" viewBox="0 0 26 40" aria-hidden="true"><ellipse cx="13" cy="9" rx="11" ry="7" fill="#5fb2e8"/><rect x="8" y="9" width="10" height="14" fill="#4aa2dc"/><line x1="13" y1="23" x2="11" y2="38" stroke="#888" stroke-width="2"/></svg>
    <div class="story__photos">
      <div class="story__photo photo--stuart-before" role="img" aria-label="Before photo of Stuart outdoors"></div>
      <div class="story__photo photo--stuart-after" role="img" aria-label="After photo of Stuart"></div>
    </div>
    <div class="pill" style="left:42px">Before</div>
    <div class="pill" style="left:200px">After</div>
    <div class="story__caption">
      <div class="story__name">Stuart Parker</div>
      <div class="story__detail">Retired Police Officer</div>
      <div class="story__detail">Age - 52</div>
    </div>
  </article>

  <p class="tagline tagline--one">Get your body looking exactly how you</p>
  <p class="tagline tagline--two">want it to look and more importantly... <span class="tagline__keep">KEEP IT THAT WAY</span></p>

  <p class="headline headline--coach">Wellness &amp; Body Transformation Coach<br>Call Robbie for a FREE and unique body<br>evaluation tailored to YOU.</p>

  <svg class="swoosh" viewBox="0 0 818 140" preserveAspectRatio="none" aria-hidden="true">
    <path d="M0 108 C250 36 540 2 818 20 L818 140 L0 140 Z" fill="#f4f4f4"/>
    <path d="M0 118 C250 44 500 8 760 8" fill="none" stroke="#ffffff" stroke-width="4"/>
  </svg>

  <p class="contact contact--phone">07700 900 418</p>
  <p class="contact contact--social">Profile: Robbie Brennan</p>
</main>
</body>
</html>
```